Fresh and Modern Real Estate Land Website

This Real Estate Agent sells only land.
The wordpress design will need to work well with responsive Avada theme.
Colors should complement the attached Home-Header.jpg, the Sonoran Desert, Southwest Region of Arizona and Tucson.
Home page layout to include
- Logo Attached: NewLogo.png
- Agent Photo: AdaMorton.jpg
- Contact Detials: use Phone
- Slogan: "I've Never Shown a House"
- Static header or Main image (see Attached Home-Header.jpg) - The dimensions of this shot may not be correct for your design. Please select from similar stock if needed and provide stock photo id.
- Intro/Welcome Text See Attached: Intro.txt
- Vertical or Horizontal display of "New" listings (include: Photo, Price, exerpt/intro) see: Properties.zip
- Tools of the trade. Home page will have a section called "Tools Of the Trade" These are items the agent uses in her work. This seciton will need to be 3 or More Images about 100 characters of text and Title. These will rotate through about 12 different tools. see: tools-of-the-trade.zip
Footer to include Contact Info/Recent Blog Posts/Testimonial
No Social Network icons
Main Menu:
Home
Properties
Testimonials
Services
About Ada
Blog
Contact
Real Estate
- Marck Script google/Times new Roman is logo. Designers Choice.

```html
<!DOCTYPE html>
<html lang="en">
<head>
<meta charset="utf-8">
<title>Ada Morton – Tucson Land</title>
<link href="https://fonts.googleapis.com/css2?family=Roboto:ital,wght@0,300;0,400;0,500;1,300;1,400&display=swap" rel="stylesheet">
<style>
:root{
  --orange:#ee6a1c;
  --blue:#1a8fd6;
  --text:#6b6b6b;
  --dark:#3a3a3a;
  --darker:#2a2a2a;
  --light:#f1f1f1;
  --white:#ffffff;
}
*{box-sizing:border-box;margin:0;padding:0}
html,body{width:743px;height:1200px;overflow:hidden}
body{font-family:"Roboto",Arial,sans-serif;background:var(--white);position:relative;color:var(--text)}
.abs{position:absolute}

/* header */
.site-header{position:absolute;left:0;top:0;width:743px;height:56px;background:#fafafa;border-bottom:1px solid #e6e6e6}
.brand{position:absolute;left:46px;top:16px;display:flex;align-items:center;gap:6px;font-size:18px;font-weight:500;color:var(--orange)}
.brand-dot{width:10px;height:10px;border-radius:50%;background:var(--orange)}
.main-nav{position:absolute;left:220px;top:23px;display:flex;gap:0;font-size:8.5px;color:#444}
.main-nav span{padding:0 9px;position:relative}
.main-nav .current{color:var(--blue)}
.main-nav .current::after{content:"";position:absolute;left:0;right:0;top:14px;height:3px;background:var(--blue)}
.phone-box{position:absolute;left:581px;top:16px;width:116px;height:22px;border:1px solid #ddd;background:#fff;display:flex;align-items:center;gap:4px;padding-left:8px;font-size:7.5px;color:#333;font-weight:500}
.phone-box b{color:var(--orange);font-size:11px;font-weight:400}

/* hero */
.hero{position:absolute;left:0;top:56px;width:743px;height:274px;background:linear-gradient(180deg,#1f8fd9 0%,#5bb3e8 30%,#a89a6e 48%,#7a7a4a 62%,#5c6b38 80%,#4a5a2c 100%)}
.hero h1{position:absolute;left:0;width:743px;top:90px;text-align:center;color:#fff;font-weight:500;font-size:38px;text-shadow:0 2px 4px rgba(0,0,0,.35)}
.hero-btn{position:absolute;left:321px;top:152px;width:101px;height:28px;border:2px solid var(--orange);background:rgba(60,40,20,.45);color:#fff;font-size:11px;font-weight:500;display:flex;align-items:center;justify-content:center}
.hero svg{position:absolute}

/* welcome */
.welcome h2{position:absolute;top:358px;left:0;width:743px;text-align:center;color:var(--orange);font-weight:400;font-size:16px}
.welcome .lead{position:absolute;top:388px;left:0;width:743px;text-align:center;color:var(--blue);font-size:8px}
.welcome .body{position:absolute;top:404px;left:46px;width:651px;text-align:center;font-size:8px;line-height:13px}

/* tools */
.tools{position:absolute;left:0;top:459px;width:743px;height:303px;background:var(--light)}
.tools h2{position:absolute;top:21px;width:743px;text-align:center;color:var(--orange);font-weight:400;font-size:16px}
.tool{position:absolute;top:57px;width:200px;text-align:center}
.tool-circle{width:109px;height:109px;border-radius:50%;background:#fff;margin:0 auto;display:flex;align-items:center;justify-content:center}
.tool-art{width:72px;height:46px;border-radius:8px}
.tool h3{color:var(--blue);font-weight:400;font-size:14px;margin-top:14px}
.tool p{font-size:8px;line-height:13px;margin-top:5px}
.pager{position:absolute;top:271px;width:20px;height:20px;border-radius:50%;border:1px solid #bbb;background:#fff}

/* listings */
.listings-title{position:absolute;left:46px;top:784px;color:var(--orange);font-weight:400;font-size:17px}
.listing{position:absolute;top:816px;width:149px}
.listing-photo{width:149px;height:98px;border:2px solid #ddd}
.price{margin-top:9px;font-size:12px;color:#333}
.price b{color:var(--blue);font-weight:500}
.listing p,.agent p{font-size:7.6px;line-height:13px;margin-top:3px}
.more{display:block;margin-top:8px;font-size:7.6px;color:var(--orange);font-weight:500}
.agent{position:absolute;left:548px;top:786px;width:149px;height:212px;border:1px solid #e2e2e2;background:#f7f7f7;padding:8px 10px}
.agent h3{color:var(--orange);font-weight:400;font-size:16px}
.agent-photo{margin-top:4px;width:132px;height:78px;background:linear-gradient(90deg,#c9302c 0%,#b04a4e 35%,#4f6d9c 60%,#3d5d8f 100%)}

/* footer */
.site-footer{position:absolute;left:0;top:1018px;width:743px;height:150px;background:var(--dark)}
.fcol{position:absolute;top:16px;font-size:7.2px;font-style:italic;font-weight:300;color:#cfcfcf}
.fcol h4{font-style:normal;font-weight:400;font-size:10px;color:#fff;margin-bottom:6px}
.fcol li{list-style:none;padding:5px 0;border-bottom:1px solid #4a4a4a}
.fcol li:last-child{border:0}
.fcol .by{color:var(--blue);display:block;margin:4px 0 8px}
.fcol .sep{border-top:1px solid #4a4a4a;padding-top:8px}
.fcol .name{color:var(--blue);font-size:9px;font-weight:400}
.fcol .hl{color:var(--orange)}
.fdiv{position:absolute;top:1038px;width:1px;height:110px;background:#555}
.bottom-bar{position:absolute;left:0;top:1168px;width:743px;height:32px;background:var(--darker);font-size:7px;font-style:italic;color:#999}
.bottom-bar .copy{position:absolute;left:46px;top:12px}
.bottom-bar .copy span{color:var(--orange)}
.bottom-bar .legal{position:absolute;right:46px;top:12px}
</style>
</head>
<body>

<header class="site-header">
  <div class="brand"><span class="brand-dot"></span>Ada Morton</div>
  <nav class="main-nav">
    <span class="current">Home</span><span>Properties</span><span>Testimonials</span><span>Services</span><span>About Ada</span><span>Blog</span><span>Contact</span>
  </nav>
  <div class="phone-box">
    <svg width="11" height="11" viewBox="0 0 12 12"><circle cx="6" cy="6" r="5.3" fill="none" stroke="#333" stroke-width="0.8"/><path d="M4 3.3c.4-.3.8-.2 1 .2l.4.9c.1.3 0 .5-.2.7l-.3.2c.3.8.9 1.4 1.6 1.7l.2-.3c.2-.2.4-.3.7-.2l.9.4c.4.2.5.6.2 1-.6.8-1.6.8-2.6.1C4.7 7.3 4 6.3 3.7 5.3c-.2-.8 0-1.5.3-2z" fill="#333"/></svg>
    Tel: <b>555-014-2290</b>
  </div>
</header>

<section class="hero" role="img" aria-label="Sonoran desert landscape with saguaro cacti and red rock mountains under a blue sky">
  <h1>I've Never Shown a House</h1>
  <div class="hero-btn">READ MORE</div>
  <svg style="left:46px;top:112px" width="28" height="44" viewBox="0 0 28 44"><polyline points="24,2 4,22 24,42" fill="none" stroke="rgba(255,255,255,.7)" stroke-width="3"/></svg>
  <svg style="left:669px;top:112px" width="28" height="44" viewBox="0 0 28 44"><polyline points="4,2 24,22 4,42" fill="none" stroke="rgba(255,255,255,.7)" stroke-width="3"/></svg>
  <svg style="left:359px;top:210px" width="26" height="16" viewBox="0 0 26 16"><polyline points="2,2 13,13 24,2" fill="none" stroke="#fff" stroke-width="2"/></svg>
</section>

<section class="welcome">
  <h2>Welcome to the Land Lady</h2>
  <p class="lead">When you are looking for Tucson land, Ada Morton's experience has "landed" her among the top 1/2% ranking of all Realtors, and that's just selling LAND!</p>
  <p class="body">Ada is proud to say that she STILL has never sold a house... but she does know the best who do. 90% of real estate is sold by 10% of the Realtors and, during nearly 30 years of selling, Ada knows and is good friends with these 10%. Utilize Ada's contacts so she can match up the right home agent...for YOU!</p>
</section>

<section class="tools">
  <h2>Tools Of the Trade</h2>
  <div class="tool" style="left:48px">
    <div class="tool-circle"><div class="tool-art" role="img" aria-label="Compass with leather pouch" style="background:linear-gradient(135deg,#5a3a26,#2a1a10)"></div></div>
    <h3>Compas</h3>
    <p>Aliquam molestie, mi et imperdiet euismod, dui purus auctor tellus, et interdum lacus lectus et ante. Sed accumsan sollicitudin sapien, sit amet adipiscing turpis gravida ac.</p>
  </div>
  <div class="tool" style="left:273px">
    <div class="tool-circle"><div class="tool-art" role="img" aria-label="Roll of orange flagging tape" style="background:linear-gradient(135deg,#ff5a2a,#e83a10)"></div></div>
    <h3>Orange Tape</h3>
    <p>Aliquam molestie, mi et imperdiet euismod, dui purus auctor tellus, et interdum lacus lectus et ante. Sed accumsan sollicitudin sapien, sit amet adipiscing turpis gravida ac.</p>
  </div>
  <div class="tool" style="left:494px">
    <div class="tool-circle"><div class="tool-art" role="img" aria-label="Yellow measuring tape reel" style="background:linear-gradient(135deg,#f2d21a,#3a3a3a)"></div></div>
    <h3>Tape-Measure</h3>
    <p>Aliquam molestie, mi et imperdiet euismod, dui purus auctor tellus, et interdum lacus lectus et ante. Sed accumsan sollicitudin sapien, sit amet adipiscing turpis gravida ac.</p>
  </div>
  <svg class="pager" style="left:349px" viewBox="0 0 20 20"><polyline points="11.5,6 7.5,10 11.5,14" fill="none" stroke="#555" stroke-width="1.3"/></svg>
  <svg class="pager" style="left:375px" viewBox="0 0 20 20"><polyline points="8.5,6 12.5,10 8.5,14" fill="none" stroke="#555" stroke-width="1.3"/></svg>
</section>

<h2 class="listings-title">New Listings</h2>
<article class="listing" style="left:46px">
  <div class="listing-photo" role="img" aria-label="Desert sunset over land parcel" style="background:linear-gradient(180deg,#c47a10 0%,#f2b020 45%,#8a4a08 80%,#2a1504 100%)"></div>
  <div class="price">Price: <b>$120, 23 00</b></div>
  <p>Aliquam molestie, mi et imperdiet euismod, dui purus auctor tellus, et interdum lacus lectus et ante.</p>
  <span class="more">More Details</span>
</article>
<article class="listing" style="left:213px">
  <div class="listing-photo" role="img" aria-label="Desert lot with mountains in the distance" style="background:linear-gradient(180deg,#8fb0d0 0%,#b8c4c8 30%,#7d8a62 55%,#6a6f4a 100%)"></div>
  <div class="price">Price: <b>$120, 23 00</b></div>
  <p>Aliquam molestie, mi et imperdiet euismod, dui purus auctor tellus, et interdum lacus lectus et ante.</p>
  <span class="more">More Details</span>
</article>
<article class="listing" style="left:381px">
  <div class="listing-photo" role="img" aria-label="Cactus-covered desert parcel with mountains" style="background:linear-gradient(180deg,#6d9cd0 0%,#a6b8c8 30%,#8a8a64 55%,#6f6a4c 100%)"></div>
  <div class="price">Price: <b>$120, 23 00</b></div>
  <p>Aliquam molestie, mi et imperdiet euismod, dui purus auctor tellus, et interdum lacus lectus et ante.</p>
  <span class="more">More Details</span>
</article>

<aside class="agent">
  <h3>Agent</h3>
  <div class="agent-photo" role="img" aria-label="Portrait of agent Ada Morton"></div>
  <p>Aliquam molestie, mi et imperdiet euismod, dui purus auctor tellus, et interdum lacus lectus et ante. Sed accumsan sollicitudin sapien, sit amet adipiscing turpis gravida ac.</p>
  <span class="more">Read More</span>
</aside>

<footer class="site-footer">
  <div class="fcol" style="left:46px;width:180px">
    <h4>Recent Blog Posts</h4>
    <ul>
      <li>Aenean a nibh eget turpis dolore magna aliquam</li>
      <li>Vehicula tempus ac sed massa dolore magna aliquam</li>
      <li>Vestibulum dolor nulla ultrices ac dolore</li>
      <li>Tincidunt sed, laoreet non est dolore magna aliquam</li>
      <li>Aenean lacinia sodalesdolore magna aliquam</li>
    </ul>
  </div>
  <div class="fcol" style="left:270px;width:190px;line-height:10px">
    <h4>Testimonials</h4>
    <p>Aenean a nibh eget turpis vestibulum ante ipsum primis in faucibus orci luctus et ultrices posuere cubilia..</p>
    <span class="by">-Name goes here</span>
    <p class="sep">Aenean a nibh eget turpis vestibulum ante ipsum primis in faucibus orci luctus et ultrices posuere cubilia..</p>
    <span class="by">-Name goes here</span>
  </div>
  <div class="fcol" style="left:506px;width:190px;line-height:11px">
    <h4>Contact Info</h4>
    <div class="name">Ada Morton</div>
    <p>4120 Saguaro Lane<br>Tucson, AZ 85718</p>
    <p style="margin-top:3px">Ph: <span class="hl">555-014-2290</span></p>
    <p style="margin-top:3px">Email: <span class="hl">info@adamorton.com</span></p>
    <p style="margin-top:6px;color:var(--blue)">Get Direction</p>
  </div>
</footer>
<div class="fdiv" style="left:243px"></div>
<div class="fdiv" style="left:486px"></div>

<div class="bottom-bar">
  <div class="copy">Copyright © 2014.<span>AdaMorton</span>. All Right Reserved</div>
  <div class="legal">Term of Services &nbsp;|&nbsp; Privacy Policy</div>
</div>

</body>
</html>
```